Bright Path Attorneys Billboard Design for Personal Injury Law Firm

Need a billboard design that we can use for different versions. 1400px X 400px jpeg or png
I have attached the logo and the attorney for the billboard. Attorney Marla Benning
Here is a link to our current website brightpathlegalgroup.example

HEADLINE: HIT BY A TRUCK?
SUBHEAD: NO FEE. BIG FIGHT.
877-GRANTLY

HEADLINE: ACCIDENT?
SUBHEAD: NO FEE, UNLESS WE WIN!
877-GRANTLY

HEADLINE: BIG TRUCK. BIG CASE.
SUBHEAD: YOU PAY $0 UPFRONT
877-GRANTLY

Target Market(s)

People in Car Accident

Industry/Entity Type

Personal Injury Attorneys

```html
<!DOCTYPE html>
<html lang="en">
<head>
<meta charset="utf-8">
<title>Bright Path Attorneys Billboard</title>
<link rel="stylesheet" href="https://fonts.googleapis.com/css2?family=Anton&family=Montserrat:wght@500&family=Roboto+Condensed:wght@500&display=swap">
<style>
  :root {
    --navy: #0f1d4a;
    --navy-deep: #0b1530;
    --ink: #000000;
    --white: #ffffff;
    --lime: #6be22a;
    --slate: #3d4148;
  }
  html, body { margin: 0; padding: 0; overflow: hidden; background: var(--white); }
  .billboard {
    position: relative;
    width: 1200px;
    height: 343px;
    overflow: hidden;
    background: var(--white);
  }
  .backdrop { position: absolute; inset: 0; }
  .attorney-photo {
    position: absolute;
    left: 40px;
    top: 10px;
    width: 300px;
    height: 333px;
    border-radius: 120px 120px 0 0;
    background: linear-gradient(180deg, #c9a57a 0%, #b48a62 35%, #1c2550 60%, #0f1d4a 100%);
  }
  .headline {
    position: absolute;
    left: 380px;
    top: 32px;
    margin: 0;
    font-family: "Anton", "Impact", sans-serif;
    font-weight: 400;
    font-size: 112px;
    line-height: 106px;
    color: var(--ink);
    letter-spacing: 1px;
    text-transform: uppercase;
  }
  .subhead {
    position: absolute;
    left: 382px;
    top: 258px;
    margin: 0;
    font-family: "Anton", "Impact", sans-serif;
    font-weight: 400;
    font-style: italic;
    font-size: 44px;
    line-height: 1;
    color: var(--ink);
    transform: skewX(-8deg);
  }
  .brand {
    position: absolute;
    left: 905px;
    top: 78px;
    display: flex;
    align-items: center;
    gap: 10px;
    font-family: "Montserrat", sans-serif;
    font-weight: 500;
    font-size: 24px;
    color: var(--slate);
    letter-spacing: 0.5px;
  }
  .brand-mark { width: 14px; height: 14px; border-radius: 50%; background: var(--lime); }
  .contact { position: absolute; left: 872px; top: 168px; width: 300px; text-align: center; }
  .phone {
    display: block;
    font-family: "Anton", "Impact", sans-serif;
    font-size: 58px;
    line-height: 1;
    color: var(--white);
    letter-spacing: 1px;
  }
  .website {
    display: block;
    margin-top: 6px;
    font-family: "Roboto Condensed", sans-serif;
    font-weight: 500;
    font-size: 21px;
    color: var(--lime);
    letter-spacing: 1px;
  }
</style>
</head>
<body>
<div class="billboard">
  <svg class="backdrop" width="1200" height="343" viewBox="0 0 1200 343" aria-hidden="true">
    <defs>
      <linearGradient id="limeFade" x1="0" y1="1" x2="0" y2="0">
        <stop offset="0" stop-color="#6be22a"/>
        <stop offset="0.7" stop-color="#6be22a"/>
        <stop offset="1" stop-color="#6be22a" stop-opacity="0"/>
      </linearGradient>
      <linearGradient id="navyShade" x1="0" y1="0" x2="1" y2="0">
        <stop offset="0" stop-color="#0b1530"/>
        <stop offset="1" stop-color="#13235a"/>
      </linearGradient>
    </defs>
    <polygon points="0,0 105,0 0,260" fill="#0b1530"/>
    <polygon points="130,0 372,0 238,343 0,343 0,330" fill="url(#navyShade)"/>
    <polygon points="110,72 365,72 255,343 22,343" fill="url(#limeFade)"/>
    <polygon points="760,343 845,155 872,155 788,343" fill="url(#limeFade)"/>
    <polygon points="913,0 1200,0 1200,63 888,63" fill="#0f1d4a"/>
    <polygon points="860,133 1200,133 1200,343 785,343" fill="url(#navyShade)"/>
  </svg>

  <div class="attorney-photo" role="img" aria-label="Portrait of attorney Marla Benning in a navy blazer, arms crossed"></div>

  <h1 class="headline">Big Truck.<br>Big Case.</h1>
  <p class="subhead">YOU PAY $0 UPFRONT</p>

  <div class="brand"><span class="brand-mark"></span><span>Bright Path Attorneys</span></div>

  <div class="contact">
    <span class="phone">877-GRANTLY</span>
    <span class="website">brightpathlegalgroup.example</span>
  </div>
</div>
</body>
</html>
```